Fun Language School in San Diego, CA - We want cool Business Card

We need a new business card design for our new logo. We are a language school in beautiful San Diego, California. Our target is students from all over the world who age from 18 to 25. They come to our school to learn English. Our school has a modern look, trending and fun place. We are the only language school who use tablets in class. We are student oriented, Students Come First is our slogan. We are re-branding ourselves with a new logo. We would like to see a designs that use our new logo and it should reflect the feel of young, fun, modern, high-tech and attractive to young people.
I've seen some business card designs with transparent look, unusual shapes, we are open to any cool ideas. Thank you very much!

In order for you to know more about our school, here are the links to our Youtube Channel and Facebook.

Youtube: https://www.vidloop.example/channel/ZXpo84kR-21bvn5wQ7t2LmHd
Facebook: https://www.friendspace.example/TVSchool

Target Market(s)

Our target is students from all over the world who age from 18 to 25. International students.

Industry/Entity Type

School

Font styles to use
Sans Serif

Requirements
Must have
• Our new logo. Name, title and address.
Should not have
• Other colors other than the ones we have in our logo. Characters are fine.

```html
<!DOCTYPE html>
<html lang="en">
<head>
<meta charset="utf-8">
<title>Harborview School – Business Card</title>
<link href="https://fonts.googleapis.com/css2?family=Arimo:wght@400;700&display=swap" rel="stylesheet">
<style>
  :root {
    --page-bg: #e9e7e4;
    --bezel: #111111;
    --bezel-edge: #3a3a3a;
    --screen-top: #c9d0ee;
    --screen-mid: #6f78c8;
    --screen-bottom: #262c8e;
    --white: #ffffff;
    --logo-teal: #3a9fa6;
    --logo-ink: #5a6470;
    --text-soft: rgba(255, 255, 255, 0.82);
  }

  * { box-sizing: border-box; margin: 0; padding: 0; }

  html, body {
    width: 1200px;
    height: 913px;
    overflow: hidden;
    background: var(--page-bg);
    font-family: "Arimo", Arial, sans-serif;
  }

  .business-card {
    position: absolute;
    left: 162px;
    top: 206px;
    width: 876px;
    height: 500px;
    border-radius: 56px;
    background: var(--bezel);
    box-shadow: inset 0 0 0 3px var(--bezel-edge), 0 18px 40px rgba(0, 0, 0, 0.25);
  }

  .screen {
    position: absolute;
    left: 92px;
    top: 62px;
    width: 692px;
    height: 376px;
    background: linear-gradient(170deg, var(--screen-top) 0%, var(--screen-mid) 55%, var(--screen-bottom) 100%);
    overflow: hidden;
  }

  .logo-band {
    position: absolute;
    left: 0;
    top: 70px;
    width: 300px;
    height: 82px;
    background: var(--white);
    display: flex;
    align-items: center;
    gap: 14px;
    padding-left: 22px;
  }

  .logo-dot {
    width: 46px;
    height: 46px;
    border-radius: 50%;
    background: var(--logo-teal);
    flex: none;
  }

  .logo-name {
    font-size: 24px;
    font-weight: 400;
    color: var(--logo-ink);
    letter-spacing: -0.3px;
    white-space: nowrap;
  }

  .social-list {
    position: absolute;
    left: 402px;
    top: 56px;
    list-style: none;
    display: flex;
    flex-direction: column;
    gap: 12px;
  }

  .social-item {
    display: flex;
    align-items: center;
    gap: 10px;
    font-size: 17px;
    color: var(--white);
    white-space: nowrap;
  }

  .social-square {
    width: 40px;
    height: 40px;
    border-radius: 7px;
    background: var(--white);
    flex: none;
  }

  .holder {
    position: absolute;
    left: 40px;
    bottom: 48px;
    color: var(--white);
  }

  .holder-name {
    font-size: 46px;
    font-weight: 400;
    line-height: 1;
    letter-spacing: 0.5px;
  }

  .holder-title {
    font-size: 24px;
    font-weight: 400;
    color: var(--text-soft);
    margin-top: 4px;
  }
</style>
</head>
<body>
  <article class="business-card">
    <div class="screen">
      <div class="logo-band">
        <span class="logo-dot"></span>
        <span class="logo-name">Harborview School</span>
      </div>

      <ul class="social-list">
        <li class="social-item"><span class="social-square"></span>/TVSchool</li>
        <li class="social-item"><span class="social-square"></span>/user/HarborviewTalks</li>
      </ul>

      <div class="holder">
        <p class="holder-name">JOHN DOE</p>
        <p class="holder-title">company owner</p>
      </div>
    </div>
  </article>
</body>
</html>
```